Redesign of Business Card to look more professional and stand out

Business card design. You can lean more about our company by going to dkrfabworks.example. Raised letters would be nice. Company name & Address
DK&R
418 Wendlow Ridge Drive, Suite 340
Harlan Falls, AL 35990

You can use my name and title: Glenn Harwick
Business Development Manager

Target Market(s)

Heavy Industrial market, i.e. utilities, chemical plants, paper mills, construction companies

Industry/Entity Type

Construction

Contact Information for Business Card

We provide Project Management & Project Support Services

Font styles to use
Serif

Requirements
Must have
• Company name & Address
• DK&R
• 418 Wendlow Ridge Drive, Suite 340
• Harlan Falls, AL 35990
Nice to have
• ideas for the back of the card
Should not have
• no crazy colors. needs to look professional and standout.

```html
<!DOCTYPE html>
<html lang="en">
<head>
<meta charset="utf-8">
<title>DK&amp;R Business Card</title>
<link href="https://fonts.googleapis.com/css2?family=Mulish:wght@400;800&display=swap" rel="stylesheet">
<style>
  :root {
    --page-bg: #e9ebf1;
    --navy: #1c3466;
    --steel-blue: #4f74ad;
    --band-blue: #5a80b8;
    --card-light: #eef0f2;
    --rule-grey: #c9ccd2;
    --shade-grey: #9a9ea5;
    --ink: #2a2f3a;
    --white: #ffffff;
  }
  html, body {
    margin: 0;
    width: 1200px;
    height: 797px;
    overflow: hidden;
    background: var(--page-bg);
    font-family: "Mulish", sans-serif;
  }
  .card-spread {
    position: absolute;
    top: 244px;
    left: 40px;
    display: flex;
    gap: 40px;
  }
  .card {
    width: 540px;
    height: 309px;
    display: block;
    box-shadow: 0 6px 18px rgba(30, 40, 70, 0.18);
  }
  .logo-word { font-family: "Mulish", sans-serif; font-weight: 800; }
  .contact-name { font-weight: 800; letter-spacing: 0.5px; }
  .contact-text { font-weight: 400; }
</style>
</head>
<body>
  <div class="card-spread">
    <svg class="card card-front" viewBox="0 0 540 309" xmlns="http://www.w3.org/2000/svg">
      <defs>
        <linearGradient id="site-photo-tone" x1="0" y1="0" x2="1" y2="1">
          <stop offset="0" stop-color="#8e9aa8"/>
          <stop offset="0.5" stop-color="#6d7c8e"/>
          <stop offset="1" stop-color="#9fb3c9"/>
        </linearGradient>
      </defs>
      <rect class="front-base" width="540" height="309" fill="var(--steel-blue)"/>
      <polygon class="front-navy-field" points="330,0 540,0 540,309 205,309" fill="var(--navy)"/>
      <polygon class="front-logo-band" points="0,178 268,178 235,258 0,258" fill="var(--band-blue)"/>
      <polygon class="front-photo" role="img" aria-label="Photo of two engineers in hard hats and safety vests overlooking an industrial plant"
               points="0,24 418,24 372,134 0,134" fill="url(#site-photo-tone)"/>
      <polygon class="front-photo-veil" points="0,108 383,108 372,134 0,134" fill="var(--white)" opacity="0.18"/>
      <text class="logo-word" x="36" y="232" font-size="46" fill="var(--white)">DK&amp;R</text>
    </svg>

    <svg class="card card-back" viewBox="0 0 540 309" xmlns="http://www.w3.org/2000/svg">
      <rect class="back-base" width="540" height="309" fill="var(--card-light)"/>
      <line class="back-divider" x1="252" y1="44" x2="252" y2="262" stroke="var(--rule-grey)" stroke-width="1"/>
      <rect class="back-strip-grey" x="0" y="296" width="292" height="13" fill="var(--shade-grey)"/>
      <polygon class="back-strip-navy" points="284,309 296,284 540,284 540,309" fill="var(--navy)"/>

      <text class="logo-word" x="30" y="186" font-size="62" fill="var(--navy)">DK&amp;R</text>

      <text class="contact-name" x="272" y="86" font-size="15" fill="var(--navy)">GLENN HARWICK</text>
      <text class="contact-text" x="272" y="103" font-size="10.5" fill="var(--ink)">Business Development Manager</text>

      <g class="contact-line phone">
        <rect x="272" y="131" width="12" height="12" rx="2.5" fill="var(--navy)"/>
        <path d="M275.3 133.6c.4 2.8 2.3 4.9 5 5.7l1-1.3-1.6-.9-.7.7c-1.1-.5-1.9-1.4-2.3-2.4l.7-.7-.9-1.6z" fill="var(--white)"/>
        <text class="contact-text" x="292" y="141" font-size="11" fill="var(--ink)">205-555-0147</text>
      </g>
      <g class="contact-line email">
        <rect x="272" y="149" width="12" height="12" rx="2.5" fill="var(--navy)"/>
        <rect x="274.5" y="152" width="7" height="5.5" fill="none" stroke="var(--white)" stroke-width="0.9"/>
        <path d="M274.5 152l3.5 3 3.5-3" fill="none" stroke="var(--white)" stroke-width="0.9"/>
        <text class="contact-text" x="292" y="159" font-size="11" fill="var(--ink)">info@dkrfabworks.example</text>
      </g>
      <g class="contact-line web">
        <rect x="272" y="167" width="12" height="12" rx="2.5" fill="var(--navy)"/>
        <circle cx="278" cy="173" r="3.6" fill="none" stroke="var(--white)" stroke-width="0.9"/>
        <path d="M274.4 173h7.2M278 169.4c-1.6 2.2-1.6 5 0 7.2M278 169.4c1.6 2.2 1.6 5 0 7.2" fill="none" stroke="var(--white)" stroke-width="0.7"/>
        <text class="contact-text" x="292" y="177" font-size="11" fill="var(--ink)">www.dkrfabworks.example</text>
      </g>

      <g class="contact-address">
        <text class="contact-text" x="292" y="210" font-size="11" fill="var(--ink)">418 Wendlow Ridge Drive</text>
        <text class="contact-text" x="292" y="225" font-size="11" fill="var(--ink)">Suite 340, Harlan Falls</text>
        <text class="contact-text" x="292" y="240" font-size="11" fill="var(--ink)">AL 35990</text>
      </g>
    </svg>
  </div>
</body>
</html>
```